I need a website built for my modeling agency company.

On our website, a user can create a profile and we will submit it to thousands of modeling agents throughout the country.

In many cases, they will receive multiple offers from modeling agencies which allows them to pick and choose the contract that is best for them to launch their modeling career.

Some tag lines to consider using:

"Submit your profile to hundreds of modeling agents instantly!"

"Get found and become a star!"

We are: The Runway Guild.

Our Slogan: The World''s Largest Network of Fashion Models and Agents

What We Do: We are an agency with one of the largest networks of fashion professionals that are looking for new modeling talent. We host professional profiles for aspiring models, professional fashion models seeking work, modeling talent seekers, and top modeling agencies. We connect aspiring models with the top modeling agencies in the United States and abroad.

By submitting your FREE profile, you will be instantly introduced to the industry’s leading modeling agents. Within a few days, you could receive multiple, competing offers from modeling agencies that all want to launch your modeling career. Receiving multiple signing offers puts you in control of deciding which contract best suites you!

Reason: I've seen some good designs, but none that are 100% perfect. These are the ones that I like best so far (to give you some ideas): http://files.pixelvane.example/img/510372/820114/820114_4917263_510372_image.jpg http://files.pixelvane.example/img/510372/829305/829305_4926851_510372_image.jpg http://files.pixelvane.example/img/510372/51847/51847_4924097_510372_image.jpg http://files.pixelvane.example/img/510372/51847/51847_4919856_510372_image.jpg http://files.pixelvane.example/img/510372/823670/823670_4920438_510372_image.jpg

Target Market(s)

Aspiring models (mostly female, but some male)

Industry/Entity Type

Modeling Agency

Colors

Designer to choose colors to be used in the design.

Requirements
Nice to have
• Somewhere in the top half of the page, I would like there to be a small form for the visitor to fill out. This form will look as follows:

Title: Instantly contact hundreds of modeling agents who are looking for new talent and could make you a star!
Fields: First Name*, Last Name*, Age, Zip Code, Email Address*, Daytime Phone, Evening Phone, Comments.

Then, there will be a "submit" button to proceed to next step of form. Just below the "submit" button, should be the following verbiage: "You will have the opportunity to upload photo(s) and provide other pertinent information in next step."

```html
<!DOCTYPE html>
<html lang="en">
<head>
<meta charset="utf-8">
<title>The Runway Guild</title>
<link href="https://fonts.googleapis.com/css2?family=Source+Sans+3:wght@400;600;700&family=Tinos&display=swap" rel="stylesheet">
<style>
:root{
  --black:#000;
  --ink:#0b0b0b;
  --nav:#9a9a9a;
  --white:#fff;
  --light:#e8e2e2;
  --panel:rgba(70,0,10,.55);
  --field:rgba(60,0,8,.55);
  --field-line:#5a0710;
  --marker:#3a0208;
  --pink:#e0408a;
  --yellow:#ffe36b;
  --grey:#a8a8a8;
  --foot-text:#666;
  --foot-red:#d9263a;
}
*{margin:0;padding:0;box-sizing:border-box}
html,body{width:979px;height:1200px;overflow:hidden;background:var(--black)}
body{position:relative;font-family:"Source Sans 3",sans-serif;color:var(--white)}
.abs{position:absolute}

.site-header{left:0;top:0;width:979px;height:80px;background:var(--ink)}
.brand{left:126px;top:20px}
.brand-name{font-size:22px;font-weight:600;letter-spacing:.5px;color:var(--white);line-height:1}
.brand-tagline{font-size:8px;color:var(--white);margin-top:6px}
.main-nav a{position:absolute;top:38px;font-family:"Tinos",serif;font-size:17px;color:var(--nav);text-decoration:none;letter-spacing:.3px}

.hero{left:0;top:80px;width:979px;height:714px;
  background:linear-gradient(90deg,#b0123e 0%,#d11f4e 14%,#5a0412 30%,#8a0a22 45%,#c4184a 62%,#e0336a 78%,#f2a020 92%,#ffe24a 100%)}
.hero-model{left:110px;top:0;width:260px;height:714px;
  background:linear-gradient(180deg,rgba(60,20,20,.35),rgba(40,180,210,.35) 55%,rgba(60,20,20,.3))}
.signup-panel{left:413px;top:119px;width:516px;height:636px;background:var(--panel)}
.marker{width:21px;background:var(--marker)}
.signup-title{left:469px;top:142px;width:420px;font-size:17px;line-height:23px;text-transform:uppercase}
.signup-title strong{font-size:21px;font-style:italic}
.field{height:40px;background:var(--field);border:1px solid var(--field-line);
  font-size:15px;color:#cfc0c0;padding-left:12px;line-height:38px}
.btn-next{left:469px;top:463px;width:88px;height:38px;background:#2a0a0c;font-size:16px;font-weight:600;color:#ddd;line-height:38px;padding-left:19px}
.signup-note{left:469px;top:512px;width:410px;font-size:15px;line-height:20px;color:#eee}
.welcome-title{left:471px;top:592px;font-size:22px;font-weight:700}
.welcome-text{left:470px;top:628px;width:420px;font-size:15px;line-height:20px;text-transform:uppercase;color:#e4d4d4}
.btn-read{left:754px;top:698px;width:132px;height:33px;background:linear-gradient(90deg,#2a0a0e,#6a2830);
  font-size:16px;font-weight:600;line-height:33px;text-align:center}
.btn-read span,.more span{color:var(--yellow)}
.more span.pink{color:var(--pink)}

.section-title{font-family:"Tinos",serif;font-size:19px;color:#bbb;letter-spacing:.5px}
.dotted{height:0;border-top:2px dotted #888}
.toggle{width:15px;height:15px;border-radius:50%;background:var(--pink);border:2px solid #f3c6d8}
.news-icon{width:18px;height:16px;background:#6c8a86;border:1px solid #a9c2bd}
.news-title{font-size:13px;font-weight:700;color:var(--white);letter-spacing:.3px}
.news-text{font-size:12.5px;line-height:18px;color:#aaa;width:320px}
.news-text a{color:var(--pink)}
.more{font-size:16px;font-weight:600;color:var(--white)}
.more i{font-style:normal;font-size:9px;color:#666;margin-right:10px}
.thumb{width:211px;height:87px;border-bottom:6px solid var(--grey)}

.site-footer{left:0;top:1120px;width:979px;height:80px;background:linear-gradient(180deg,#d8d8d8,#fff 30%,#fff)}
.footer-links{top:22px;width:979px;text-align:center;font-size:11px;color:var(--foot-text)}
.footer-links .active{color:var(--foot-red)}
.copyright{top:41px;width:979px;text-align:center;font-size:11px;color:var(--foot-text)}
</style>
</head>
<body>
<header class="site-header abs">
  <div class="brand abs">
    <div class="brand-name">The Runway Guild</div>
    <div class="brand-tagline">The World's Largest Network of Fashion Models and Agents</div>
  </div>
  <nav class="main-nav">
    <a style="left:471px">HOME</a><a style="left:558px">BIO</a><a style="left:626px">FOLIO</a><a style="left:714px">GALLERY</a><a style="left:832px">CONTACT</a>
  </nav>
</header>

<section class="hero abs" role="img" aria-label="Stage backdrop of red, pink and gold light curtains">
  <div class="hero-model abs" role="img" aria-label="Fashion model in a turquoise dress"></div>
</section>
<div class="signup-panel abs"></div>
<div class="marker abs" style="left:427px;top:144px;height:49px"></div>
<h1 class="signup-title abs" style="font-weight:400">Instantly contact hundreds of modeling agents who are looking for new talent and could make you a <strong>Star!</strong></h1>
<div class="field abs" style="left:469px;top:228px;width:196px">First Name</div>
<div class="field abs" style="left:680px;top:228px;width:197px">Last Name</div>
<div class="field abs" style="left:469px;top:274px;width:196px">Area</div>
<div class="field abs" style="left:680px;top:274px;width:197px">Zip Code</div>
<div class="field abs" style="left:469px;top:319px;width:408px">Email Address</div>
<div class="field abs" style="left:469px;top:367px;width:196px">Daytime Phone</div>
<div class="field abs" style="left:680px;top:367px;width:197px">Evening Phone</div>
<div class="field abs" style="left:469px;top:414px;width:408px">Email Address</div>
<div class="btn-next abs">Next &gt;</div>
<p class="signup-note abs">"You will have the opportunity to upload photo(s) and provide other pertinent information in next step."</p>
<div class="marker abs" style="left:427px;top:591px;height:48px"></div>
<h2 class="welcome-title abs">WELCOME TO MY WEB SITE!</h2>
<p class="welcome-text abs">We are an agency with one of the largest networks of fashion professionals that are looking for new modeling talent.</p>
<div class="btn-read abs">read <span>more</span></div>

<section class="news">
  <h3 class="section-title abs" style="left:64px;top:823px;font-weight:400">NEWS &amp; EVENTS</h3>
  <div class="toggle abs" style="left:405px;top:826px"></div>
  <div class="dotted abs" style="left:64px;top:853px;width:362px"></div>
  <div class="news-icon abs" style="left:70px;top:881px"></div>
  <div class="news-title abs" style="left:102px;top:881px">Fusce interdum. Maecenas eu elit</div>
  <p class="news-text abs" style="left:102px;top:898px">Morbi volutpat leo in ligula. Inter vel magna. sagittis. <a>Fusce interdum. Sed laoreet.</a> Aenean. Sed laoreet. Aenean pede.</p>
  <div class="dotted abs" style="left:64px;top:966px;width:362px"></div>
  <div class="news-icon abs" style="left:70px;top:984px"></div>
  <div class="news-title abs" style="left:102px;top:984px">Fusce interdum. Maecenas eu elit</div>
  <p class="news-text abs" style="left:102px;top:1001px"><a>Fusce interdum. Sed laoreet lorem ipsum.</a> Morbi volutpat leo in ligula. Inter vel magna. sagittis. Aenean. Sed laoreet. Aenean pede.</p>
  <div class="dotted abs" style="left:64px;top:1069px;width:362px"></div>
  <div class="more abs" style="left:315px;top:1082px"><i>::</i>more <span class="pink">news</span></div>
</section>

<section class="gallery">
  <h3 class="section-title abs" style="left:462px;top:823px;font-weight:400">PHOTO GALLERY</h3>
  <div class="toggle abs" style="left:892px;top:826px"></div>
  <div class="dotted abs" style="left:462px;top:853px;width:451px"></div>
  <div class="thumb abs" style="left:468px;top:880px;background:linear-gradient(90deg,#f2ece6,#b07a5a)" role="img" aria-label="Model posing on white sheets"></div>
  <div class="thumb abs" style="left:691px;top:880px;background:linear-gradient(90deg,#e9c89a,#a8683e)" role="img" aria-label="Close beauty portrait"></div>
  <div class="thumb abs" style="left:468px;top:980px;background:linear-gradient(90deg,#5a5e66,#2a2c30)" role="img" aria-label="Model with flowing dark hair"></div>
  <div class="thumb abs" style="left:691px;top:980px;background:linear-gradient(90deg,#f2e8d6,#c8b08a)" role="img" aria-label="Male model in a light suit"></div>
  <div class="more abs" style="left:800px;top:1082px"><i>::</i>view <span class="pink">more</span></div>
</section>

<footer class="site-footer abs">
  <div class="footer-links abs"><span class="active">HOME</span> | BIO | FOLIO | GALLERY | NEWS | CONTACTS</div>
  <div class="copyright abs">Copyright © Your Company Name</div>
</footer>
</body>
</html>
```